Belmora Wines

Hi all,

My name’s Tom Welling and I run a small wine brand based in the Canberra Wine District, Australia. I’m currently in the process of branding the business and am looking for a designer to help develop a new visual direction.

Background
I’ll be growing my own fruit from a leased vineyard site Named 'Ashbrook' and my family’s property named 'Tallin Park', with a stronger emphasis on organic practices and site expression.

The Direction
The brand will centre around single vineyard wines, with each wine reflecting the unique site it comes from. I’d like the branding to support this idea of place, origin, and authenticity.

In terms of visual style, I’m drawn to something that is:

Simple and effective
A balance between traditional and modern
Clean, considered, and not overly decorative

Nothing too over-the-top, the goal is something timeless that lets the wine and vineyard story speak for itself.

At this stage, I’m mainly looking for:

Conceptual design direction / ideas
Label design (with potential to expand into broader branding)

I’m open to creative interpretation, so if the story resonates with you, I’d love to see how you would approach it.

Below I've attached an example of the bottle shape I will be using.

Cheers,
Tom

Colors
0054AA
0677BA
7BADD7
CADEEF
E8F1F8
FFC000
F8CF3A
FAE287
FDF2CF
FEFAEE

Requirements
Must have
• Mix of modern and traditional

```html
<!DOCTYPE html>
<html lang="en">
<head>
<meta charset="utf-8">
<title>Belmora Wines – Riesling Label</title>
<link rel="stylesheet" href="https://fonts.googleapis.com/css2?family=Playfair+Display:wght@400;500;600;700&display=swap">
<style>
  :root {
    --backdrop: #2b2827;
    --label: #161514;
    --gold: #c9a24e;
    --silver: #9a9796;
    --caption: #8f8b8a;
  }
  * { margin: 0; padding: 0; box-sizing: border-box; }
  html, body {
    width: 1200px;
    height: 1200px;
    overflow: hidden;
    background: var(--backdrop);
  }
  .label {
    position: absolute;
    left: 160px;
    top: 150px;
    width: 880px;
    height: 900px;
    background: var(--label);
    font-family: "Playfair Display", Georgia, serif;
  }
  .vineyard {
    position: absolute;
    top: 146px;
    left: 0;
    width: 100%;
    text-align: center;
    font-size: 18px;
    font-weight: 600;
    letter-spacing: 0.22em;
    color: var(--caption);
    text-transform: uppercase;
  }
  .brand {
    position: absolute;
    top: 185px;
    left: 0;
    width: 100%;
    text-align: center;
    font-size: 124px;
    font-weight: 600;
    line-height: 1;
    color: var(--gold);
    letter-spacing: -0.01em;
  }
  .variety {
    position: absolute;
    top: 498px;
    left: 0;
    width: 100%;
    text-align: center;
    font-size: 44px;
    font-weight: 600;
    letter-spacing: 0.85em;
    padding-left: 0.85em;
    color: var(--silver);
  }
  .details {
    position: absolute;
    top: 760px;
    left: 193px;
    right: 191px;
    display: flex;
    justify-content: space-between;
    font-size: 22px;
    font-weight: 500;
    color: var(--caption);
  }
</style>
</head>
<body>
  <main class="label">
    <p class="vineyard">Tallin Park Vineyard</p>
    <h1 class="brand">Belmora</h1>
    <h2 class="variety">Riesling</h2>
    <div class="details">
      <span class="abv">11.5% ALC/VOL</span>
      <span class="volume">750 ml</span>
    </div>
  </main>
</body>
</html>
```